Tech Startup Needs Business Card Design

I am looking for an eye catching business card design for our new company, Torn Kite. We are a place for business owners and contractors to share their experiences with their customers and check their current customers. Our website, www.torn-kite.co, may be able to offer some guidance as to the design.

Industry/Entity Type

Business

Contact Information for Business Card

Owen Barthwick
888-417-3083
Owen@torn-kite.co
www.torn-kite.co

```html
<!DOCTYPE html>
<html lang="en">
<head>
<meta charset="utf-8">
<title>Torn Kite – Business Card</title>
<link href="https://fonts.googleapis.com/css2?family=Josefin+Sans:wght@400;600&display=swap" rel="stylesheet">
<style>
  :root {
    --backdrop: #3d3d3d;
    --card: #ffffff;
    --ink: #2b2b2b;
    --brand-red: #e5191f;
    --panel-dark: #262626;
    --panel-light: #ececec;
    --frame: #5a5a5a;
    --rule-grey: #5c5c5c;
    --text-light: #f2f2f2;
  }
  * { margin: 0; padding: 0; box-sizing: border-box; }
  html, body {
    width: 1200px; height: 800px; overflow: hidden;
    background: var(--backdrop);
    font-family: "Josefin Sans", sans-serif;
  }
  .card {
    position: absolute;
    left: 350px; width: 498px; height: 284px;
    background: var(--card);
  }
  .card--front { top: 86px; }
  .card--back { top: 423px; }

  .front-wordmark {
    position: absolute; inset: 0;
    display: flex; align-items: center; justify-content: center; gap: 16px;
    color: var(--ink);
    font-size: 58px; font-weight: 400; letter-spacing: 0.5px;
  }
  .front-wordmark .mark-dot {
    width: 46px; height: 46px; border-radius: 50%;
    background: var(--brand-red);
  }

  .back-frame {
    position: absolute; left: 35px; top: 27px; width: 429px; height: 230px;
    border: 1px solid var(--frame);
    overflow: hidden;
  }
  .back-frame .texture {
    position: absolute; left: 0; top: 0; width: 212px; height: 100%;
    background: var(--panel-light);
  }
  .back-frame .corner {
    position: absolute; left: 0; top: 0; width: 0; height: 0;
    border-top: 18px solid var(--brand-red);
    border-right: 18px solid transparent;
  }
  .back-frame .divider-band {
    position: absolute; left: 212px; top: 0; width: 6px; height: 100%;
    background: var(--brand-red);
  }
  .back-frame .info-panel {
    position: absolute; left: 218px; top: 0; right: 0; height: 100%;
    background: var(--panel-dark);
  }
  .logo-tile {
    position: absolute; left: 28px; top: 36px; width: 157px; height: 157px;
    background: #fff;
    display: flex; flex-direction: column; align-items: center; justify-content: center; gap: 14px;
  }
  .logo-tile .mark-dot {
    width: 54px; height: 54px; border-radius: 50%; background: var(--brand-red);
  }
  .logo-tile .name {
    color: var(--brand-red); font-size: 27px; font-weight: 400;
  }

  .icon-badge {
    position: absolute; left: 199px; width: 30px; height: 30px;
    border-radius: 50%; background: #fff;
    border: 3px solid var(--brand-red);
    display: flex; align-items: center; justify-content: center;
  }
  .icon-badge svg { width: 15px; height: 15px; }
  .icon-badge--person { top: 28px; }
  .icon-badge--phone { top: 104px; }
  .icon-badge--web { top: 143px; }

  .contact-name {
    position: absolute; left: 253px; top: 35px;
    color: var(--text-light); font-size: 20px; font-weight: 400; letter-spacing: 0.5px;
  }
  .contact-rule {
    position: absolute; left: 253px; top: 82px; width: 142px; height: 1px;
    background: linear-gradient(to right, var(--brand-red) 0 26px, var(--rule-grey) 26px);
  }
  .contact-line {
    position: absolute; left: 253px;
    color: var(--text-light); font-size: 12.5px; letter-spacing: 0.3px;
  }
  .contact-line--phone { top: 112px; }
  .contact-line--email { top: 151px; }
</style>
</head>
<body>
  <section class="card card--front">
    <div class="front-wordmark"><span class="mark-dot"></span><span>Torn Kite</span></div>
  </section>

  <section class="card card--back">
    <div class="back-frame">
      <div class="texture" role="img" aria-label="Subtle light grey diagonal texture"></div>
      <div class="corner"></div>
      <div class="info-panel"></div>
      <div class="divider-band"></div>

      <div class="logo-tile">
        <span class="mark-dot"></span>
        <span class="name">Torn Kite</span>
      </div>

      <div class="icon-badge icon-badge--person">
        <svg viewBox="0 0 16 16" fill="#222"><circle cx="8" cy="5" r="3.2"/><path d="M2 15c0-3.6 2.7-5.6 6-5.6s6 2 6 5.6z"/></svg>
      </div>
      <div class="icon-badge icon-badge--phone">
        <svg viewBox="0 0 16 16" fill="#222"><path d="M3.6 1.2l2.3 2.9-1.3 1.8c.9 1.9 2.4 3.4 4.3 4.4l1.8-1.3 2.9 2.3-1.2 2.6C7.4 13.6 2.4 8.6 1 3.6z"/></svg>
      </div>
      <div class="icon-badge icon-badge--web">
        <svg viewBox="0 0 16 16" fill="none" stroke="#222" stroke-width="1.2"><circle cx="8" cy="8" r="6.5"/><ellipse cx="8" cy="8" rx="2.8" ry="6.5"/><path d="M1.5 8h13M2.6 4.6h10.8M2.6 11.4h10.8"/></svg>
      </div>

      <p class="contact-name">OWEN BARTHWICK</p>
      <div class="contact-rule"></div>
      <p class="contact-line contact-line--phone">888-417-3083</p>
      <p class="contact-line contact-line--email">Owen@torn-kite.co</p>
    </div>
  </section>
</body>
</html>
```